Flyer Design job - Occupational Therapy Flyer!

We are looking for a flyer design.
SPECIFICATIONS:
Size: 8 1/2 x 11, bleeds .125 inches all around.
CMYK colors only. One sided print.

THE COMPANY:
The clientele is an all boys school.
- We do not want any photos of kids, or people.
- Attached is the image we want to use, along with their logo and copy.

Here is the copy as well: Copy for flyer:
The Brightfield Academy is excited to welcome (This is the name of the boys school that will not have occupational services offered in their school).
Tot Haven PT (logo)
We’re proud to provide your child with professional occupational therapy services right in his school. The familiar environment paired with our expert and caring therapists will give your son the chance to grow and thrive without leaving his comfort zone.
• Mrs. Dena Morvitz, OTR/L, Director of Occupational Therapy Services Working in private practice for over 19 years
• Fully equipped therapy gym
• No transportation necessary (no missing Yeshiva or work)
• Introductory low rates for evaluations and therapy sessions
• Communication and collaboration with the parents, Principals, Rebbeim, teachers, and other therapists
• Therapy is exclusive to The Brightfield Academy, servicing boys from primary through eighth grade.

(Highlighted text:) Private therapy in a school setting

Call or email now to schedule your evaluation
555-218-4093 tothavenpt4@mailbox-example.com
Tot Haven PT • PO Box 913 • Lakewood NJ 00000

Target Market(s)

Parent of school aged boys. (preschool - 8th grade).

Colors

Designer to choose colors to be used in the design.

Requirements
Must have
• My logo, copy, the image i supplied. It should be well laid out, with nice typography, easy to read, and look fun.
• It must be able to be saved down to CS6. Adobe suite.
• CMYK
Should not have
• It should not look "girly".
• No images of people or kids.

```html
<!DOCTYPE html>
<html lang="en">
<head>
<meta charset="utf-8">
<title>Brightfield Academy – Occupational Therapy Flyer</title>
<link rel="stylesheet" href="https://fonts.googleapis.com/css2?family=Source+Sans+3:ital,wght@0,600;1,600;1,700&family=PT+Sans+Narrow&display=swap">
<style>
  :root {
    --page-bg: #dedede;
    --teal: #006363;
    --teal-dark: #0e3a36;
    --teal-line: #1aa8a0;
    --orange: #f7a21b;
    --orange-line: #f47c20;
    --gold-line: #8a7a3a;
    --white: #ffffff;
    --photo-top: #d9d8cc;
    --photo-mid: #4a4fb8;
    --photo-low: #3336a6;
  }
  * { margin: 0; padding: 0; box-sizing: border-box; }
  html, body {
    width: 1200px; height: 1200px; overflow: hidden;
    background: var(--page-bg);
  }
  .flyer {
    position: absolute; left: 230px; top: 121px;
    width: 740px; height: 958px;
    background: var(--teal-dark);
    overflow: hidden;
    font-family: "Source Sans 3", sans-serif;
    color: var(--white);
  }
  .flyer-shapes { position: absolute; inset: 0; }
  .headline {
    position: absolute; left: 0; right: 0; top: 430px;
    text-align: center;
    font-style: italic; font-weight: 700;
    font-size: 52px; line-height: 55px;
    color: var(--orange);
    letter-spacing: -0.3px;
  }
  .intro {
    position: absolute; left: 20px; right: 20px;
    text-align: center;
    font-style: italic; font-weight: 600;
    font-size: 17px; line-height: 22px;
  }
  .intro-one { top: 555px; }
  .intro-two { top: 620px; }
  .benefits {
    position: absolute; left: 40px; top: 741px; width: 370px;
    list-style: none;
    font-family: "PT Sans Narrow", sans-serif;
    font-size: 14.5px; line-height: 19px;
  }
  .benefits li { position: relative; padding-left: 14px; }
  .benefits li::before {
    content: ""; position: absolute; left: 1px; top: 6px;
    width: 7px; height: 7px; background: var(--teal-line);
    transform: rotate(45deg);
  }
  .brand {
    position: absolute; left: 400px; width: 310px; top: 810px;
    text-align: center;
  }
  .brand-name {
    font-weight: 700; font-size: 42px; line-height: 46px;
    color: var(--orange);
  }
  .brand-contact {
    margin-top: 8px;
    font-style: italic; font-weight: 700;
    font-size: 17px; line-height: 22px;
  }
</style>
</head>
<body>
<main class="flyer">
  <svg class="flyer-shapes" width="740" height="958" viewBox="0 0 740 958">
    <defs>
      <linearGradient id="gymTones" x1="0" y1="0" x2="0" y2="1">
        <stop offset="0" stop-color="var(--photo-top)"/>
        <stop offset="0.35" stop-color="#c9c8bb"/>
        <stop offset="0.55" stop-color="var(--photo-mid)"/>
        <stop offset="1" stop-color="var(--photo-low)"/>
      </linearGradient>
    </defs>
    <rect class="gym-photo" role="img" aria-label="Photo of a therapy gym with a hanging tire swing, trapeze bar, padded blue mats, foam steps, a therapy ball and a small tent" x="0" y="0" width="740" height="420" fill="url(#gymTones)"/>
    <path class="band-teal" d="M0 382 C180 370 400 360 509 357 C600 362 680 390 740 410 L740 720 C700 712 650 700 600 693 L0 689 Z" fill="var(--teal)"/>
    <path class="line-orange" d="M0 382 C180 370 400 360 509 357 C600 362 680 390 740 410" fill="none" stroke="var(--orange-line)" stroke-width="3"/>
    <path class="line-teal" d="M0 427 C250 402 430 384 500 383 C600 388 680 430 740 466" fill="none" stroke="var(--teal-line)" stroke-width="3"/>
    <path class="line-gold" d="M0 689 L600 693 C650 700 700 712 740 720" fill="none" stroke="var(--gold-line)" stroke-width="3"/>
  </svg>

  <h1 class="headline">The Brightfield Academy<br>is excited to welcome</h1>

  <p class="intro intro-one">We’re proud to provide your child with professional occupational therapy<br>services right in his school.</p>
  <p class="intro intro-two">The familiar environment paired with our expert and caring therapists will give your<br>son the chance to grow and thrive without leaving his comfort zone.</p>

  <ul class="benefits">
    <li>Mrs. Dena Morvitz, OTR/L, Director of Occupational Therapy Services<br>Working in private practice for over 19 years</li>
    <li>Fully equipped therapy gym</li>
    <li>No transportation necessary (no missing Yeshiva or work)</li>
    <li>Introductory low rates for evaluations and therapy sessions</li>
    <li>Communication and collaboration with the parents, Principals,<br>Rebbeim, teachers, and other therapists</li>
    <li>Therapy is exclusive to the Brightfield Academy, servicing boys from<br>primary through eighth grade.</li>
  </ul>

  <div class="brand">
    <div class="brand-name">Tot Haven PT</div>
    <p class="brand-contact">PO Box 913 • Lakewood NJ 00000<br>555-218-4093</p>
  </div>
</main>
</body>
</html>
```